New VORANEX keyboard

We need to redesign the plastic cover of electronic keyboard. The equipment is a cooker with an agitation system. See page http://www.delvano-kitchentech.example/catering-machinery/industrial-kitchens-equipment/tilting-bratt-pan where you can even find a video.

One of the important features of this equipment is the mixing system. We need to give more importance on the keypad and renew all buttons and general design.

Note: On the manual instruction you can find the keypad description. The keys 13, 14 and 15 can be moved. The rest (1-12) must remain on same postion.

Reason: Uploaded dimensions (mm 95x150) and logo

Industry/Entity Type

Electronic

```html
<!DOCTYPE html>
<html lang="en">
<head>
<meta charset="utf-8">
<title>DELVANO keypad</title>
<link rel="stylesheet" href="https://fonts.googleapis.com/css2?family=Roboto:wght@300&family=Roboto+Condensed:wght@700&display=swap">
<style>
  :root {
    --panel-top: #262626;
    --panel-bottom: #151515;
    --header-top: #3b86e6;
    --header-bottom: #0f3f95;
    --key-light: #4a8ff0;
    --key-dark: #0a2a70;
    --key-ring: #d8dde6;
    --key-gap: #101010;
    --guide-line: rgba(70, 160, 190, 0.35);
    --screen-edge: #c9ccd0;
    --screen-fill: #000000;
    --ink: #ffffff;
    --header-ink: #dfe8f7;
  }
  * { box-sizing: border-box; margin: 0; padding: 0; }
  html, body { width: 758px; height: 1200px; overflow: hidden; background: var(--panel-bottom); }
  .keypad {
    position: relative; width: 758px; height: 1200px; overflow: hidden;
    background: linear-gradient(180deg, var(--panel-top), var(--panel-bottom));
  }
  .brand-bar {
    position: absolute; left: 0; top: 0; width: 100%; height: 56px;
    background: linear-gradient(180deg, var(--header-top), var(--header-bottom));
    display: flex; align-items: center; justify-content: center;
    font-family: "Roboto", sans-serif; font-weight: 300; font-size: 28px;
    letter-spacing: 16px; color: var(--header-ink); padding-left: 16px;
  }
  .guide { position: absolute; left: 0; width: 100%; height: 2px; background: var(--guide-line); }
  .display {
    position: absolute; left: -8px; top: 230px; width: 380px; height: 356px;
    border: 4px solid var(--screen-edge); border-radius: 22px; background: var(--screen-fill);
  }
  .key {
    position: absolute; width: 92px; height: 92px; margin: -46px 0 0 -46px;
    border-radius: 50%; border: 3px solid var(--key-ring); padding: 4px; background: var(--key-gap);
  }
  .key-face {
    width: 100%; height: 100%; border-radius: 50%;
    background: radial-gradient(circle at 50% 25%, var(--key-light), var(--key-dark) 95%);
    display: flex; align-items: center; justify-content: center; flex-direction: column;
    color: var(--ink); font-family: "Roboto Condensed", sans-serif; font-weight: 700;
    font-size: 16px; line-height: 1.15; text-align: center;
  }
  .key-face svg { width: 50px; height: 50px; }
  .reset-key {
    position: absolute; left: 286px; top: 842px; width: 212px; height: 212px; border-radius: 50%;
    background: radial-gradient(circle at 45% 25%, var(--key-light), var(--key-dark) 100%);
    border: 3px solid rgba(255,255,255,0.15);
  }
  .reset-label {
    position: absolute; left: 478px; top: 920px; width: 138px; height: 54px; border-radius: 27px;
    background: linear-gradient(180deg, var(--key-light), var(--key-dark));
    color: var(--ink); font-family: "Roboto Condensed", sans-serif; font-weight: 700; font-size: 25px;
    display: flex; align-items: center; justify-content: center;
  }
</style>
</head>
<body>
<main class="keypad">
  <header class="brand-bar">DELVANO</header>

  <div class="guide" style="top:139px"></div>
  <div class="guide" style="top:498px"></div>
  <div class="guide" style="top:708px"></div>

  <div class="display"></div>

  <!-- top row -->
  <div class="key" style="left:124px;top:134px"><div class="key-face">
    <svg viewBox="0 0 50 50"><rect x="22" y="8" width="6" height="34" rx="2" fill="#fff"/></svg></div></div>
  <div class="key" style="left:296px;top:134px"><div class="key-face">
    <svg viewBox="0 0 50 50"><path d="M8 14 L26 28 L26 20 L42 36" stroke="#fff" stroke-width="5" fill="none" stroke-linejoin="round"/></svg></div></div>
  <div class="key" style="left:467px;top:134px"><div class="key-face">
    <svg viewBox="0 0 50 50" fill="none" stroke="#fff" stroke-width="2.5"><path d="M9 18 q8 -6 16 0 t16 0"/><path d="M9 25 q8 -6 16 0 t16 0"/><path d="M9 32 q8 -6 16 0 t16 0"/><path d="M14 40 L38 10" stroke-width="2"/></svg></div></div>
  <div class="key" style="left:639px;top:134px"><div class="key-face">START<br>STOP</div></div>

  <!-- right column -->
  <div class="key" style="left:467px;top:308px"><div class="key-face">
    <svg viewBox="0 0 50 50"><path d="M8 36 L25 14 L42 36" stroke="#fff" stroke-width="8" fill="none" stroke-linejoin="miter"/></svg></div></div>
  <div class="key" style="left:639px;top:308px"><div class="key-face">
    <svg viewBox="0 0 50 50" fill="none" stroke="#fff" stroke-width="3"><path d="M9 19 q8 -6 16 0 t16 0"/><path d="M9 27 q8 -6 16 0 t16 0"/><path d="M9 35 q8 -6 16 0 t16 0"/></svg></div></div>
  <div class="key" style="left:467px;top:485px"><div class="key-face">
    <svg viewBox="0 0 50 50"><path d="M8 16 L25 38 L42 16" stroke="#fff" stroke-width="8" fill="none"/></svg></div></div>
  <div class="key" style="left:639px;top:485px"><div class="key-face">
    <svg viewBox="0 0 50 50" fill="#fff"><rect x="23" y="6" width="4" height="22"/><rect x="23" y="25" width="16" height="4"/><circle cx="9" cy="27" r="3"/><circle cx="25" cy="42" r="3"/><circle cx="41" cy="27" r="3" opacity="0"/></svg></div></div>

  <!-- bottom row -->
  <div class="key" style="left:124px;top:708px"><div class="key-face">
    <svg viewBox="0 0 50 50" fill="none" stroke="#fff" stroke-width="2.5"><path d="M12 24 L40 18 L42 34 L16 40 Z"/><path d="M10 8 L22 20 M22 20 L22 13 M22 20 L15 20"/></svg></div></div>
  <div class="key" style="left:296px;top:708px"><div class="key-face">
    <svg viewBox="0 0 50 50" fill="none" stroke="#fff" stroke-width="2.5"><path d="M18 14 L40 8 L42 32 L20 38 Z"/><path d="M26 26 L10 38 M10 38 L17 38 M10 38 L10 31"/></svg></div></div>
  <div class="key" style="left:467px;top:708px"><div class="key-face">MIXER<br>I/O</div></div>
  <div class="key" style="left:639px;top:708px"><div class="key-face">
    <svg viewBox="0 0 50 50" fill="none" stroke="#fff" stroke-width="4"><path d="M17 40 V10 M10 17 L17 10 L24 17"/><path d="M33 10 V40 M26 33 L33 40 L40 33"/></svg></div></div>

  <!-- reset -->
  <div class="reset-key"></div>
  <div class="reset-label">RESET</div>
</main>
</body>
</html>
```